Website Design for Solar Panel Company

We are working with a company called VoltaryNX.

Some sites to use for content/competitors and inspiration:
https://www.brightmoor.example
https://prod.cld-prod.raylumen.example
https://amberfieldvolt.example
https://www.korvane.example/solarpanels

Thank you for taking the time to consider designing a website for us. We are web developers based in Stockton, CA, USA. Most of our projects go through the same process. Understanding this process may help you win a project with us. We custom-code all of our websites in-house. We don’t have any requirements as to what tools you use for your design, but we prefer Figma files. For any design that we label as four-stars, we send it to the client for review. The client picks the final design they want us to use. Once we complete this process, we will continue to show additional clients all the four-star sites and purchase them later. Your designs will have multiple chances to sell. For better chances of success, we ask that you follow these guidelines.

IMAGES:
If you use any images or icons in the design, we ask that you have a link to the asset so we can purchase the image/icon. Most of the designs we submit do not have the customer’s images on them unless they have some great images. Be creative; show us the feeling you are trying to portray with your image choices. Use any royalty-free site you choose. We subscribe to Quillex and mainly use their images, but we can purchase images outside of Quillex. PLEASE NOTE: we will not submit designs to clients with watermarks on the images.

FONTS:
We ask that you identify the fonts used in the design. This can be done in a message if you want. We typically use Marlowe Fonts and Quillex Fonts.

CONTENT:
We're always open to different content and ideas. We often submit designs with stock images so the client can see our vision. We typically take pictures after the website launch to use their images with our vision. Lorem Ipsum is fine for paragraphs, but we ask that you write the headers in correct English. We want to be able to show the vision and identify the sections of the website.

INSPIRATION:
We typically add a couple of links in the brief of websites we like to help you get started in your design.

REVISIONS:
We do not often ask for revisions of the designs unless we see something in the design that may not appeal to the client. If there are slight changes that we want to make, we do that in the development process.

FEEDBACK:
We rarely give feedback on designs during the design process. We are working on many website projects and do not have the time to provide feedback. We usually respond if your request is well thought out and asks specific questions, but a note asking “feedback, please” usually goes unanswered.

```html
<!DOCTYPE html>
<html lang="en">
<head>
<meta charset="utf-8">
<title>VoltaryNX Energy Group</title>
<link rel="stylesheet" href="https://fonts.googleapis.com/css2?family=Lexend:wght@300;400;500;600;700&display=swap">
<style>
:root{
  --green:#3fb61a;
  --green-dark:#2a9c0c;
  --green-light:#84ea3e;
  --black:#050505;
  --ink:#1b1b1b;
  --muted:#555;
  --paper:#ffffff;
  --soft:#f2f2f2;
  --line:#d4d4d4;
}
*{margin:0;padding:0;box-sizing:border-box}
html,body{width:1200px;height:4329px;overflow:hidden}
body{font-family:"Lexend",sans-serif;color:var(--ink);background:var(--paper);position:relative}
.abs{position:absolute}
.label{font-size:11px;color:var(--green);text-transform:uppercase;letter-spacing:.5px;font-weight:400}
.h2{font-size:32px;font-weight:300;text-transform:uppercase;line-height:1.22;letter-spacing:.5px}
.h2 b{font-weight:700}
.btn{display:flex;align-items:center;justify-content:center;background:var(--green);color:#111;font-size:10px;text-transform:uppercase}
.photo{position:absolute}
.watermark{position:absolute;left:0;width:1200px;font-size:92px;font-weight:700;letter-spacing:4px;white-space:nowrap;text-align:center;line-height:1}

/* header */
.site-header{position:absolute;top:0;left:0;width:1200px;height:50px;background:var(--black);z-index:3}
.brand{position:absolute;left:120px;top:9px;color:#fff;font-weight:700;font-size:19px;line-height:1}
.brand small{display:block;font-size:9px;font-weight:300;margin-top:2px}
.nav{position:absolute;left:346px;top:19px;display:flex;gap:25px;font-size:10px;color:#fff}
.call{position:absolute;left:826px;top:12px;display:flex;align-items:center;gap:10px;color:#fff;font-size:10px;font-weight:600}
.call span{color:var(--green-light)}
.icon-dot{position:absolute;top:12px;width:26px;height:26px;border-radius:50%;background:var(--green);display:flex;align-items:center;justify-content:center}

/* hero */
.hero{position:absolute;top:50px;left:0;width:1200px;height:516px;background:linear-gradient(90deg,#2d3a2c 0%,#4f5e46 40%,#8a8c74 70%,#9ea28a 100%)}
.hero h1{position:absolute;left:120px;top:155px;color:#fff;font-size:46px;font-weight:300;line-height:1.15;letter-spacing:1px}
.hero h1 b{font-weight:600}
.hero p{position:absolute;left:121px;top:266px;width:500px;color:#fff;font-size:12px;line-height:1.4}

/* quote */
.quote{position:absolute;left:121px;top:518px;width:957px;height:142px;background:#fff;box-shadow:0 6px 16px rgba(0,0,0,.12);text-align:center}
.quote h3{margin-top:22px;font-size:18px;font-weight:500}
.quote p{font-size:9px;color:var(--muted);margin-top:6px}
.field{position:absolute;top:76px;width:256px;height:44px;border:1px solid var(--line);font-size:9px;color:#999;padding:14px 16px;text-align:left}

/* about */
.about-text p{font-size:11px;color:var(--muted);line-height:1.45}
.tick{display:flex;align-items:center;gap:10px;font-size:11px;font-weight:500}
.tick i{width:13px;height:13px;border-radius:50%;background:var(--green)}

/* services */
.services{position:absolute;top:1123px;left:0;width:1200px;height:649px;background:radial-gradient(circle at 600px 385px,#2f6e12 0,#0b1a05 230px,#000 430px),#000;color:#fff;overflow:hidden}
.services .glow{position:absolute;right:0;top:0;width:400px;height:649px;background:linear-gradient(100deg,transparent 40%,rgba(70,150,20,.55))}
.num{position:absolute;width:57px;height:57px;border-radius:50%;background:var(--green);color:#fff;font-size:26px;font-weight:300;display:flex;align-items:center;justify-content:center}
.svc{position:absolute;width:240px;font-size:10px;line-height:1.5}
.svc h4{font-size:12px;font-weight:600;margin-bottom:4px}
.svc.left{text-align:right}

/* testimonials */
.reviews{position:absolute;top:3072px;left:0;width:1200px;height:365px;background:linear-gradient(90deg,#2e9f0e,#6dd62a 100%)}
</style>
</head>
<body>

<header class="site-header">
  <div class="brand">VOLTARYNX<small>ENERGY GROUP</small></div>
  <nav class="nav"><span>SERVICES</span><span>PROJECT</span><span>BLOG</span><span>CONTACT</span></nav>
  <div class="call">
    <svg width="26" height="26" viewBox="0 0 26 26"><circle cx="13" cy="13" r="13" fill="#3fb61a"/><path d="M9 8c1 0 1.6 2 1.6 2.6 0 .8-1 1-.6 1.8.6 1.2 1.6 2.2 2.8 2.8.8.4 1-.6 1.8-.6.6 0 2.6.6 2.6 1.6 0 1-1.2 2-2.2 2C11 18.2 7.8 15 7.8 11 7.8 9.8 8 8 9 8z" fill="#fff"/></svg>
    CALL US: <span>1400 555 019</span>
  </div>
  <div class="icon-dot" style="left:1013px"><svg width="14" height="14" viewBox="0 0 14 14"><circle cx="6" cy="6" r="4.2" fill="none" stroke="#fff" stroke-width="1.6"/><path d="M9 9l3.5 3.5" stroke="#fff" stroke-width="1.6"/></svg></div>
  <div class="icon-dot" style="left:1055px"><svg width="14" height="14" viewBox="0 0 14 14"><circle cx="7" cy="4.5" r="2.8" fill="none" stroke="#fff" stroke-width="1.4"/><path d="M1.8 13c.6-3 2.6-4.4 5.2-4.4s4.6 1.4 5.2 4.4" fill="none" stroke="#fff" stroke-width="1.4"/></svg></div>
</header>

<section class="hero" role="img" aria-label="Modern house with solar panels on the roof and an open glass living room">
  <h1><b>HARNESS</b> THE <b>LIMITLESS</b><br>POWER OF <b>THE SUN</b></h1>
  <p>We're your trusted partner in the world of renewable energy, and we're excited to introduce you to a world of possibilities.</p>
  <div class="btn abs" style="left:121px;top:313px;width:119px;height:32px">LEARN MORE</div>
</section>

<section class="quote">
  <h3>GET A FREE FREE QUOTE</h3>
  <p>Our team will reply within 20 minutes, and we'll craft a custom plan for your rental property's success.</p>
  <div class="field" style="left:16px">Name</div>
  <div class="field" style="left:288px">Email</div>
  <div class="field" style="left:560px">Phone</div>
  <div class="btn abs" style="left:833px;top:76px;width:108px;height:44px">REQUEST</div>
</section>

<!-- about -->
<div class="watermark" style="top:1045px;color:#f1f1f1">VOLTARYNX ENERGY GROUP</div>
<div class="photo" style="left:112px;top:713px;width:234px;height:337px;background:linear-gradient(160deg,#7ea548,#3d6a2c 50%,#4a6fa8)" role="img" aria-label="Rows of solar panels across a green field"></div>
<div class="abs" style="left:370px;top:713px;width:160px;height:123px;background:var(--black);color:#fff;text-align:center">
  <div style="font-size:46px;font-weight:500;margin-top:22px;line-height:1">30</div>
  <div style="font-size:10px;margin-top:10px">YEAR EXPERIENCE</div>
</div>
<div class="photo" style="left:358px;top:851px;width:160px;height:224px;background:linear-gradient(170deg,#8fb0c8,#5b7d5f 60%,#2d4f3a)" role="img" aria-label="Engineer pointing at a solar panel array"></div>
<div class="about-text">
  <div class="label abs" style="left:590px;top:757px">GET TO KNOW US</div>
  <div class="h2 abs" style="left:590px;top:778px">WELCOME TO <b>VOLTARYNX<br>ENERGY GROUP</b> SERVICES</div>
  <p class="abs" style="left:591px;top:869px;width:480px">At VoltaryNX Services, we are dedicated to providing innovative and eco-friendly solutions to meet your energy needs. We believe in a future where renewable energy sources play a vital role in reducing carbon emissions and creating a sustainable planet.</p>
  <div class="tick abs" style="left:591px;top:945px"><i></i>Every day fresh and quality products</div>
  <div class="tick abs" style="left:591px;top:970px"><i></i>Don't panic go for organic</div>
  <div class="btn abs" style="left:591px;top:1007px;width:121px;height:33px">EXPLORE MORE</div>
</div>

<!-- services -->
<section class="services">
  <div class="glow"></div>
  <div class="label abs" style="left:0;width:1200px;text-align:center;top:53px">SERVICES WE OFFER</div>
  <div class="h2 abs" style="left:0;width:1200px;text-align:center;top:78px">SUSTAINABLE ENERGY <b>SERVICES</b></div>
  <p class="abs" style="left:320px;width:560px;text-align:center;top:124px;font-size:11px;line-height:1.45">The goal of sustainable energy services is to transition from traditional, fossil fuel-based energy sources to renewable energy sources, such as solar, wind, hydro, geothermal, and biomass.</p>
  <svg class="abs" style="left:440px;top:225px" width="320" height="320" viewBox="0 0 320 320">
    <circle cx="160" cy="160" r="150" fill="none" stroke="rgba(120,230,60,.25)" stroke-width="14"/>
    <circle cx="160" cy="160" r="140" fill="#fff"/>
    <path d="M112 118a78 78 0 1 0 96 0" fill="none" stroke="#1f3a0f" stroke-width="22" stroke-linecap="round"/>
    <line x1="160" y1="84" x2="160" y2="160" stroke="#1f3a0f" stroke-width="22" stroke-linecap="round"/>
  </svg>

  <div class="svc left" style="left:148px;top:226px"><h4>Wind Turbines</h4>Lorem ipsum dolor sit amet, consectetur adipiscing elit, sed do eiusmod tempor incididunt ut labore et dolore magna aliqua.</div>
  <div class="num" style="left:402px;top:222px">1</div>
  <div class="svc left" style="left:102px;top:369px"><h4>Maintenance</h4>Lorem ipsum dolor sit amet, consectetur adipiscing elit, sed do eiusmod tempor incididunt ut labore et dolore magna aliqua.</div>
  <div class="num" style="left:355px;top:365px">2</div>
  <div class="svc left" style="left:148px;top:508px"><h4>Wind Generators</h4>Lorem ipsum dolor sit amet, consectetur adipiscing elit, sed do eiusmod tempor incididunt ut labore et dolore magna aliqua.</div>
  <div class="num" style="left:402px;top:504px">3</div>

  <div class="num" style="left:740px;top:222px">6</div>
  <div class="svc" style="left:811px;top:226px"><h4>Hybrid Energy</h4>Lorem ipsum dolor sit amet, consectetur adipiscing elit, sed do eiusmod tempor incididunt ut labore et dolore magna aliqua.</div>
  <div class="num" style="left:786px;top:365px">5</div>
  <div class="svc" style="left:858px;top:369px"><h4>Solar Energy</h4>Lorem ipsum dolor sit amet, consectetur adipiscing elit, sed do eiusmod tempor incididunt ut labore et dolore magna aliqua.</div>
  <div class="num" style="left:740px;top:504px">4</div>
  <div class="svc" style="left:811px;top:508px"><h4>Solar PV Systems</h4>Lorem ipsum dolor sit amet, consectetur adipiscing elit, sed do eiusmod tempor incididunt ut labore et dolore magna aliqua.</div>
</section>

<!-- benefits -->
<section class="abs" style="top:1772px;left:0;width:1200px;height:505px;background:var(--soft);overflow:hidden">
  <div class="watermark" style="top:428px;color:#e6e6e6">VOLTARYNX ENERGY GROUP</div>
  <div class="label abs" style="left:122px;top:117px">COMPANY BENEFITS</div>
  <div class="h2 abs" style="left:121px;top:140px">GREENER <b>TOMORROW</b><br><b>FOR</b> YOUR <b>BUSINESS</b></div>
  <p class="abs" style="left:122px;top:230px;width:450px;font-size:11px;color:var(--muted);line-height:1.5">The amount of energy you use will depend on the type of business you run. However, there are lots of ways that you can save energy no matter what you do.</p>
  <div class="abs" style="left:121px;top:306px;width:144px;height:34px;border:1px solid var(--green);color:var(--green-dark);font-size:9px;display:flex;align-items:center;justify-content:center">TECHNICAL SUPPORT</div>
  <div class="btn abs" style="left:277px;top:306px;width:176px;height:34px;font-size:9px">BEST ENERGY SOLUTIONS</div>
  <div class="photo" style="left:672px;top:148px;width:160px;height:287px;background:linear-gradient(180deg,#b8c8d8,#7e93a8 45%,#3e5a8f)" role="img" aria-label="City towers behind a rooftop solar array"></div>
  <div class="photo" style="left:845px;top:61px;width:233px;height:337px;background:linear-gradient(170deg,#f4d6a6,#c7a77a 25%,#5a6a8a 60%,#34508e)" role="img" aria-label="Solar panels in a field at sunset"></div>
</section>

<!-- projects -->
<div class="label abs" style="left:0;width:1200px;text-align:center;top:2333px">OUR RECENT</div>
<div class="h2 abs" style="left:0;width:1200px;text-align:center;top:2355px">COMPLETED <b>PROJECTS</b></div>
<div class="photo" style="left:113px;top:2420px;width:317px;height:523px;background:linear-gradient(170deg,#7f9ccc,#3c5f9f 50%,#2b4a86)" role="img" aria-label="Technicians installing solar panels on a roof"></div>
<div class="photo" style="left:442px;top:2420px;width:295px;height:236px;background:linear-gradient(180deg,#f0a94a,#d88a3a 40%,#3a3e4a 70%,#2a3552)" role="img" aria-label="Solar farm under an orange sunset sky"></div>
<div class="photo" style="left:750px;top:2420px;width:337px;height:300px;background:linear-gradient(170deg,#8aa7c8,#4f6470 45%,#2d3e3a)" role="img" aria-label="Two workers carrying a panel on a metal roof"></div>
<div class="photo" style="left:442px;top:2668px;width:295px;height:275px;background:linear-gradient(180deg,#c8ccd0,#8a93a0 45%,#3e5b95)" role="img" aria-label="Rooftop solar panels with city skyline"></div>
<div class="photo" style="left:750px;top:2733px;width:337px;height:210px;background:linear-gradient(180deg,#c9a88a,#8c8f98 45%,#3d5380)" role="img" aria-label="Solar array in front of downtown buildings at dusk"></div>
<div class="btn abs" style="left:541px;top:2977px;width:118px;height:33px">EXPLORE MORE</div>

<!-- testimonials -->
<section class="reviews">
  <div class="abs" style="left:122px;top:66px;font-size:10px;color:#133a05">TESTIMONIALS</div>
  <div class="h2 abs" style="left:122px;top:90px;color:#fff">GREAT <b>REVIEWS</b> FROM<br>OUR <b>CLIENTS</b></div>
  <p class="abs" style="left:122px;top:186px;width:560px;font-size:11px;color:#fff;line-height:1.45">All of our lorries are fitted with Satellite Tracking and Temperature Controlled monitoring systems so that the transportation of high value and temperature sensitive loads can be monitored at all times.</p>
  <div class="abs" style="left:122px;top:252px;font-size:9px;color:#133a05">CO FOUNDER</div>
  <div class="abs" style="left:122px;top:265px;font-size:12px;color:#fff">Marisol Deane</div>
  <svg class="abs" style="left:122px;top:308px" width="60" height="8"><circle cx="4" cy="4" r="3" fill="#9ee06a"/><circle cx="19" cy="4" r="3" fill="#133a05"/><circle cx="34" cy="4" r="3" fill="#9ee06a"/><circle cx="49" cy="4" r="3" fill="#9ee06a"/></svg>
  <div class="photo" style="left:770px;top:0;width:316px;height:365px;background:linear-gradient(170deg,#6c8a5a,#8c7a66 40%,#b8553f 70%,#5a6a4a)" role="img" aria-label="Happy family standing outside their home"></div>
  <div class="abs" style="left:1086px;top:0;width:114px;height:365px;background:#7de83a"></div>
</section>

<!-- blog -->
<div class="label abs" style="left:0;width:1200px;text-align:center;top:3477px">BLOGS</div>
<div class="h2 abs" style="left:0;width:1200px;text-align:center;top:3500px"><b>OUR LATEST</b> ARTICLES</div>
<div class="photo" style="left:121px;top:3568px;width:470px;height:237px;background:linear-gradient(180deg,#9aa8b4,#6c7a86 45%,#2e3338)" role="img" aria-label="Two engineers walking along rows of solar panels">
  <div class="abs" style="left:28px;top:165px;font-size:10px;color:var(--green-light)">FEBRUARY 6, 2024</div>
  <div class="abs" style="left:28px;top:187px;font-size:12px;font-weight:600;color:#fff;line-height:1.35">5 TRENDS EXPECTED TO DRIVE E&amp;C INDUSTRY<br>GROWTH IN 2024</div>
</div>
<div class="photo" style="left:612px;top:3568px;width:143px;height:108px;background:linear-gradient(170deg,#8fb0d8,#3a5e9e)" role="img" aria-label="Close-up of blue solar panels"></div>
<div class="abs" style="left:772px;top:3582px;font-size:10px;color:var(--green)">FEBRUARY 6, 2024</div>
<div class="abs" style="left:772px;top:3603px;font-size:12px;font-weight:600;line-height:1.35">TRUSTED CONSTRUCTION CONSULTING<br>SERVICES FROM HARROWGATE, INC: AN<br>OVERVIEW</div>
<div class="photo" style="left:612px;top:3697px;width:143px;height:108px;background:linear-gradient(170deg,#a8c0d8,#4a6aa0 60%,#2f4680)" role="img" aria-label="Worker installing a solar panel"></div>
<div class="abs" style="left:772px;top:3720px;font-size:10px;color:var(--green)">JANUARY 31, 2024</div>
<div class="abs" style="left:772px;top:3741px;font-size:12px;font-weight:600;line-height:1.35">CONSTRUCTION OVERSIGHT: INSIGHTS<br>FROM HARROWGATE, INC.</div>

<!-- footer -->
<footer class="abs" style="top:4008px;left:0;width:1200px;height:321px;background:var(--black);overflow:hidden">
  <div class="watermark" style="top:182px;color:#111">VOLTARYNX ENERGY GROUP</div>
  <div class="abs" style="left:0;width:1200px;top:140px;text-align:center;color:#fff;font-size:25px;font-weight:700;line-height:1">VOLTARYNX<div style="font-size:12px;font-weight:300;margin-top:3px">ENERGY GROUP</div></div>
  <nav class="abs" style="left:0;width:1200px;top:202px;display:flex;justify-content:center;gap:26px;font-size:10px;color:#fff"><span>SERVICES</span><span>PROJECT</span><span>BLOG</span><span>CONTACT</span></nav>
  <div class="abs" style="left:0;top:239px;width:1200px;height:1px;background:#333"></div>
  <svg class="abs" style="left:533px;top:242px" width="134" height="26"><circle cx="13" cy="13" r="12" fill="#3fb61a"/><circle cx="49" cy="13" r="12" fill="#3fb61a"/><circle cx="85" cy="13" r="12" fill="#3fb61a"/><circle cx="121" cy="13" r="12" fill="#3fb61a"/></svg>
  <div class="abs" style="left:0;width:1200px;top:293px;text-align:center;font-size:9px;color:#fff">© 2024 Kestrel Bins Co &nbsp;|&nbsp; Privacy Policy &nbsp;|&nbsp; Terms</div>
</footer>

<section class="abs" style="left:113px;top:3884px;width:973px;height:229px;background:#fff;text-align:center">
  <div class="label" style="margin-top:46px">NEWSLETTER</div>
  <div class="h2" style="margin-top:10px"><b>SUBSCRIBE FOR LATEST</b> UPDATES</div>
  <div class="abs" style="left:217px;top:124px;width:362px;height:56px;border:1px solid var(--line);font-size:9px;color:#999;padding:22px 14px;text-align:left">Enter Email</div>
  <div class="abs" style="left:589px;top:124px;width:168px;height:56px;background:linear-gradient(90deg,var(--green-dark),var(--green-light));font-size:9px;display:flex;align-items:center;justify-content:center">SUBSCRIBE</div>
</section>

</body>
</html>
```